Mobile App UI for Telecommunications/Hosting Company

We are about to convert our existing self-service Customer Portal into a mobile phone application and need an elegant and professional UI/UX design. Our company provides telecommunication (voice/mobile/data) and hosting services to medium-sized business. The primary purpose of the application is to view trouble tickets, alerts, orders, and performance charts. This application is available to customers only - not the general public.

Please provide a UI design suitable for display on iPhone/Android devices. The attached document includes a proposed screen flow. You are free to design your own screens to display the same information elegantly.
Updates

Please note that the design should be based on the wireframes in the Word document, not the screenshots.  The screenshots are just to show our existing web portal look & feel.

Also, just a few screens are required for initial submission (3 would be great).

Thanks,
Dermot.

Target Market(s)

IT Managers away from their desk and using a mobile phone application.
Adult males from technical background aged 30-50.
Customers of Brindlewood Networks have access to this application (not the general public). This is a self-service portal for customers only.

Industry/Entity Type

Business

Colors
0592cd
33a6d7
85cae6
cadf82
fde08a

Requirements
Must have
• Please look at the screenshots from our current Customer Portal site (part of the project brief). The mobile app does not have to look the same, but should follow a similar style.

Please check out our company web site at www.brindlewoodnetworks.example (this site is not the customer portal and has a different look at feel) to understand what Brindlewood Networks does.
Nice to have
• Sharing capabilities via email/SMS.
A nice background image to make it stand out
The colours selected below are a guide only as they are similar to the corporate colours
- The priority is something that works on a phone - a design extendable to tablets is a nice to have as our existing web site looks OK on a tablet..

```html
<!DOCTYPE html>
<html lang="en">
<head>
<meta charset="utf-8">
<title>BrindleView – Mobile App Screens</title>
<link rel="stylesheet" href="https://fonts.googleapis.com/css2?family=Open+Sans:wght@300;400;600;700&display=swap">
<style>
:root{
  --page:#ececee;
  --blue-deep:#0577b0;
  --blue:#0592cd;
  --blue-mid:#33a6d7;
  --blue-light:#85cae6;
  --lime:#cadf82;
  --lime-pale:#dfeeaa;
  --lime-bright:#d6f06b;
  --menu:#0f4b5c;
  --menu-line:#1c5d6e;
  --ink:#1d3440;
  --white:#ffffff;
  --button:#1c5f8c;
}
*{box-sizing:border-box;margin:0;padding:0}
html,body{width:1200px;height:515px;overflow:hidden}
body{background:var(--page);font-family:"Open Sans",Arial,sans-serif;position:relative;color:var(--white)}
.screen{position:absolute;top:111px;width:183px;height:295px;overflow:hidden;
  background:linear-gradient(160deg,var(--blue-mid) 0%,var(--blue) 55%,var(--blue-deep) 100%)}
.screen--login{left:90px}
.screen--menu{left:367px}
.screen--news{left:645px}
.screen--ticket{left:922px}
.status-bar{position:absolute;top:0;left:0;right:0;height:10px;display:flex;align-items:center;
  justify-content:space-between;padding:0 4px;font-size:5px;color:var(--white);background:rgba(0,40,70,.25);z-index:3}
.status-bar--light{background:var(--white);color:#333}
.status-bar .time{position:absolute;left:50%;transform:translateX(-50%)}
/* login */
.brand{position:absolute;top:46px;left:0;right:0;text-align:center;font-size:11px;font-weight:400;color:var(--white);line-height:14px}
.welcome{position:absolute;top:120px;width:100%;text-align:center;font-size:5.5px;font-weight:600;color:var(--lime)}
.field{position:absolute;left:18px;width:132px;height:19px;background:var(--white);display:flex;align-items:center;gap:5px;padding-left:5px;font-size:5px;color:#aaa}
.field--user{top:137px}
.field--pass{top:165px;color:#777;font-size:8px;letter-spacing:1px}
.help-link{position:absolute;top:187px;right:32px;font-size:4px;color:var(--white);text-decoration:underline}
.remember{position:absolute;top:203px;left:18px;display:flex;align-items:center;gap:4px;font-size:4px;color:var(--white)}
.sign-in{position:absolute;top:220px;left:18px;width:132px;height:16px;background:var(--button);display:flex;align-items:center;justify-content:center;gap:3px;font-size:5px;font-weight:700;color:var(--white)}
/* menu */
.menu-panel{position:absolute;top:0;left:0;width:145px;height:100%;background:var(--menu);z-index:2}
.profile{height:26px;background:var(--white);padding:3px 10px}
.profile-name{font-size:11px;color:#222;line-height:12px}
.profile-role{font-size:5px;color:#8ab53a;margin-left:36px}
.menu-spacer{height:18px}
.menu-group{border-bottom:1px solid var(--menu-line);padding:5px 0 4px}
.menu-title{display:flex;align-items:center;gap:8px;padding-left:10px;font-size:6.5px;color:var(--lime);height:14px}
.menu-item{display:flex;align-items:center;gap:7px;padding-left:35px;font-size:5px;color:var(--lime);height:13px}
.menu-behind{position:absolute;top:0;left:145px;right:0;height:100%;background:var(--blue)}
.behind-bar{height:26px;background:var(--lime-pale)}
.behind-list{position:absolute;top:148px;left:3px;right:0;background:var(--white);color:#555;font-size:6px}
.behind-list span{display:block;padding:5px 2px;border-bottom:1px solid #ddd}
.behind-tag{position:absolute;left:3px;font-size:5px;font-weight:700;color:var(--white)}
/* header */
.app-header{position:absolute;top:10px;left:0;right:0;height:16px;background:var(--lime-pale);display:flex;align-items:center;justify-content:center;font-size:6px;color:#335}
.app-header .burger{position:absolute;left:8px;top:4px}
.app-header b{font-weight:700}
/* news */
.news-title{position:absolute;top:44px;left:9px;display:flex;align-items:center;gap:3px;font-size:10px;font-weight:300;color:var(--lime)}
.news-list{position:absolute;top:61px;left:9px;right:8px}
.news-item{margin-bottom:5px;font-size:5px;line-height:6.3px}
.news-item h3{font-size:5.5px;font-weight:700;color:var(--ink)}
.news-item .by{font-size:3px;line-height:4px;opacity:.8}
.section-label{position:absolute;left:9px;font-size:6px;color:var(--white);font-weight:300}
.feed{position:absolute;left:3px;right:3px;background:rgba(200,230,245,.35);border:1px solid rgba(255,255,255,.5);border-radius:3px;padding:1px}
.feed-row{height:15px;display:flex;align-items:center;justify-content:space-between;padding:0 6px 0 9px;font-size:4px;color:#234;background:rgba(180,222,240,.85);margin-bottom:2px}
.feed-row:last-child{margin-bottom:0}
.feed-row::after{content:"";border-left:4px solid #234;border-top:2px solid transparent;border-bottom:2px solid transparent}
/* ticket */
.tabs{position:absolute;top:42px;left:10px;right:8px;height:20px;font-size:4px;color:var(--white)}
.tab{position:absolute;top:0}
.tab--active{left:0;width:40px;height:12px;background:var(--white);color:#234;display:flex;align-items:center;justify-content:center;gap:2px;font-size:5px;z-index:1}
.tab--notes{left:58px;top:2px}
.tab--files{left:100px;top:2px}
.tab-strip{position:absolute;top:10px;left:0;right:0;height:7px;background:var(--white);display:flex;justify-content:flex-end;align-items:center;gap:6px;padding-right:5px}
.details{position:absolute;top:67px;left:8px;right:8px}
.detail{margin-bottom:8px}
.detail dt{font-size:5px;line-height:7px;font-weight:600;color:var(--white)}
.detail dd{font-size:4px;line-height:5px;color:var(--white)}
.toggle-row{position:absolute;top:193px;left:0;right:0;height:17px;border-top:1px solid rgba(255,255,255,.3);border-bottom:1px solid rgba(255,255,255,.3);display:flex;align-items:center;justify-content:space-between;padding:0 8px;font-size:5px;font-weight:600}
.toggle{width:26px;height:13px;border-radius:7px;background:var(--lime-bright);position:relative}
.toggle::after{content:"";position:absolute;right:1px;top:1px;width:11px;height:11px;border-radius:50%;background:var(--white)}
.details--lower{top:224px}
.details--lower .detail{margin-bottom:6px}
.notes{font-size:3.6px;line-height:4.5px}
</style>
</head>
<body>

<!-- Screen 1: sign in -->
<section class="screen screen--login" aria-label="Sign in screen">
  <div class="status-bar"><span>●●●●● Carrier</span><span class="time">9:23 AM</span><span>66%</span></div>
  <p class="brand">Brindlewood Networks</p>
  <p class="welcome">WELCOME TO BRINDLEVIEW</p>
  <div class="field field--user">
    <svg width="7" height="7" viewBox="0 0 10 10"><circle cx="5" cy="3" r="2.5" fill="#bbb"/><path d="M0 10a5 4 0 0 1 10 0z" fill="#bbb"/></svg>User Name or Email Address</div>
  <div class="field field--pass">
    <svg width="6" height="8" viewBox="0 0 6 10"><circle cx="3" cy="2.5" r="2" fill="none" stroke="#bbb"/><rect x="2.5" y="4" width="1" height="6" fill="#bbb"/></svg>●●●●●●</div>
  <span class="help-link">Need help logging in?</span>
  <div class="remember">
    <svg width="8" height="8" viewBox="0 0 10 10"><rect x=".5" y=".5" width="9" height="9" fill="none" stroke="#cadf82"/><path d="M2 5l2 2 5-6" fill="none" stroke="#cadf82" stroke-width="1.5"/></svg>Remember my login details</div>
  <div class="sign-in">
    <svg width="6" height="6" viewBox="0 0 10 10"><circle cx="5" cy="5" r="5" fill="#f4d03f"/><rect x="3" y="4.5" width="4" height="3" fill="#1c5f8c"/></svg>SIGN IN</div>
</section>

<!-- Screen 2: navigation menu -->
<section class="screen screen--menu" aria-label="Navigation menu">
  <div class="menu-behind">
    <div class="behind-bar"></div>
    <span class="behind-tag" style="top:136px">● HO</span>
    <div class="behind-list"><span>DNS</span><span>Patc</span><span>Acce</span><span>Host</span><span>View</span></div>
    <span class="behind-tag" style="top:273px">● TIC</span>
    <span class="behind-tag" style="top:284px">● BIL</span>
  </div>
  <nav class="menu-panel">
    <div class="profile"><p class="profile-name">R.Okafor</p><p class="profile-role">Graphic Designer</p></div>
    <div class="menu-spacer"></div>
    <div class="menu-group">
      <div class="menu-title"><svg width="9" height="9" viewBox="0 0 10 10"><path d="M0 5L10 0 7 10 5 6z" fill="#cadf82"/></svg>Tickets</div>
      <div class="menu-item"><svg width="7" height="6" viewBox="0 0 10 8"><path d="M0 1h4l1 1h5v6H0z" fill="#cadf82"/></svg>Open</div>
      <div class="menu-item"><svg width="7" height="7" viewBox="0 0 10 10"><circle cx="5" cy="5" r="4" fill="none" stroke="#cadf82" stroke-width="1.4"/><path d="M5 2.5V5h2" fill="none" stroke="#cadf82"/></svg>Recent</div>
    </div>
    <div class="menu-group">
      <div class="menu-title"><svg width="9" height="9" viewBox="0 0 10 10"><path d="M0 5L10 0 7 10 5 6z" fill="#cadf82"/></svg>Alerts</div>
      <div class="menu-item"><svg width="7" height="6" viewBox="0 0 10 8"><path d="M0 1h4l1 1h5v6H0z" fill="#cadf82"/></svg>Open</div>
      <div class="menu-item"><svg width="7" height="7" viewBox="0 0 10 10"><circle cx="5" cy="5" r="4" fill="none" stroke="#cadf82" stroke-width="1.4"/><path d="M5 2.5V5h2" fill="none" stroke="#cadf82"/></svg>Recent</div>
    </div>
    <div class="menu-group">
      <div class="menu-title"><svg width="9" height="9" viewBox="0 0 10 10"><rect x="1" y="1" width="8" height="8" fill="none" stroke="#cadf82" stroke-width="1.4"/><path d="M3 4h4M3 6h4" stroke="#cadf82"/></svg>Orders</div>
      <div class="menu-item"><svg width="7" height="6" viewBox="0 0 10 8"><path d="M0 1h4l1 1h5v6H0z" fill="#cadf82"/></svg>Open</div>
      <div class="menu-item"><svg width="7" height="7" viewBox="0 0 10 10"><circle cx="5" cy="5" r="4" fill="none" stroke="#cadf82" stroke-width="1.4"/><path d="M5 2.5V5h2" fill="none" stroke="#cadf82"/></svg>Recent</div>
    </div>
    <div class="menu-group">
      <div class="menu-title"><svg width="10" height="10" viewBox="0 0 10 10"><circle cx="5" cy="5" r="3.5" fill="none" stroke="#cadf82" stroke-width="2" stroke-dasharray="2 1"/><circle cx="5" cy="5" r="1.2" fill="#cadf82"/></svg>Services</div>
      <div class="menu-item"><svg width="7" height="7" viewBox="0 0 10 10"><circle cx="3" cy="3" r="2" fill="#cadf82"/><circle cx="7" cy="3" r="2" fill="#cadf82"/><rect x="1" y="6" width="8" height="3" fill="#cadf82"/></svg>By Family</div>
      <div class="menu-item"><svg width="7" height="7" viewBox="0 0 10 10"><circle cx="5" cy="5" r="2.5" fill="#cadf82"/><path d="M5 0v2M5 8v2M0 5h2M8 5h2" stroke="#cadf82"/></svg>By Solution</div>
      <div class="menu-item"><svg width="7" height="7" viewBox="0 0 10 10"><circle cx="4" cy="4" r="3" fill="none" stroke="#cadf82" stroke-width="1.4"/><path d="M6 6l3.5 3.5" stroke="#cadf82" stroke-width="1.5"/></svg>Search</div>
    </div>
    <div class="menu-group" style="border:0">
      <div class="menu-title"><svg width="10" height="8" viewBox="0 0 10 8"><rect width="10" height="8" fill="#cadf82"/><path d="M0 0l5 4 5-4" fill="none" stroke="#0f4b5c"/></svg>Contact</div>
    </div>
  </nav>
</section>

<!-- Screen 3: news and feeds -->
<section class="screen screen--news" aria-label="Home screen with news and feeds">
  <div class="status-bar status-bar--light"><span>●●●●● Carrier</span><span class="time">9:23 AM</span><span>66%</span></div>
  <header class="app-header">
    <svg class="burger" width="11" height="8" viewBox="0 0 11 8"><path d="M0 .5h11M0 4h11M0 7.5h11" stroke="#234" stroke-width="1.2"/></svg>
    BrindleView</header>
  <h2 class="news-title"><svg width="12" height="10" viewBox="0 0 12 10"><rect x=".5" y=".5" width="11" height="9" fill="none" stroke="#cadf82"/><rect x="2" y="2" width="3" height="3" fill="#cadf82"/><path d="M6 2.5h4M6 4.5h4M2 7h8" stroke="#cadf82"/></svg>NEWS</h2>
  <div class="news-list">
    <article class="news-item">
      <h3>A heartwarming response to a life-saving surgery.</h3>
      <p>15-year-old Kai Moreno, our latest sponsored patient from Harbour Hearts Fund, is desperately ill with a disease that is causing his heart to fail.</p>
      <p class="by">Posted by staff, 20 March 2014</p>
    </article>
    <article class="news-item">
      <h3>A heartwarming response to a life-saving surgery.</h3>
      <p>15-year-old Kai Moreno, our latest sponsored patient from Harbour Hearts Fund, is desperately ill with a disease that is causing his heart to fail.</p>
      <p class="by">Posted by staff, 20 March 2014</p>
    </article>
  </div>
  <p class="section-label" style="top:150px">Event Feeds</p>
  <div class="feed" style="top:161px">
    <div class="feed-row">consectetur adipiscing elit</div>
    <div class="feed-row">consectetur adipiscing elit</div>
    <div class="feed-row">consectetur adipiscing elit</div>
  </div>
  <p class="section-label" style="top:217px">Recently accessed</p>
  <div class="feed" style="top:229px">
    <div class="feed-row">consectetur adipiscing elit</div>
    <div class="feed-row">consectetur adipiscing elit</div>
    <div class="feed-row">consectetur adipiscing elit</div>
  </div>
</section>

<!-- Screen 4: ticket details -->
<section class="screen screen--ticket" aria-label="Ticket details screen">
  <div class="status-bar status-bar--light"><span>●●●●● Carrier</span><span class="time">9:23 AM</span><span>66%</span></div>
  <header class="app-header">
    <svg class="burger" width="11" height="8" viewBox="0 0 11 8"><path d="M0 .5h11M0 4h11M0 7.5h11" stroke="#234" stroke-width="1.2"/></svg>
    Tickets -&nbsp;<b>Details</b></header>
  <div class="tabs">
    <div class="tab tab--active">● Summary</div>
    <span class="tab tab--notes">● Notes</span>
    <span class="tab tab--files">Attachments</span>
    <div class="tab-strip">
      <svg width="5" height="4" viewBox="0 0 10 8"><rect width="10" height="8" fill="#345"/></svg>
      <svg width="5" height="5" viewBox="0 0 10 10"><path d="M2 0l2 3-1 1c1 2 2 3 3 3l1-1 3 2-2 2C4 10 0 6 0 2z" fill="#345"/></svg>
    </div>
  </div>
  <dl class="details">
    <div class="detail"><dt>Ticket ID:</dt><dd>687277 - NBAR not showing in Sydney DSL service</dd></div>
    <div class="detail"><dt>Status:</dt><dd>Approved</dd></div>
    <div class="detail"><dt>Date Logged:</dt><dd>March 27 2014 10:42 AM</dd></div>
    <div class="detail"><dt>Service ID - Service Discription:</dt><dd>MDSL788523044 - Sydney DSL 1Mbps/20Mbps</dd></div>
    <div class="detail"><dt>Solution/Site Name:</dt><dd>Sydney Office</dd></div>
    <div class="detail"><dt>Service Level:</dt><dd>Business</dd></div>
  </dl>
  <div class="toggle-row">Notification Enable: <span class="toggle"></span></div>
  <dl class="details details--lower">
    <div class="detail"><dt>Inview Alert:</dt><dd>Sydney IP Port (MYIPN123456789) - Reached 99.00%</dd></div>
    <div class="detail"><dt>Resolution Comment:</dt></div>
    <div class="detail"><dt>Recent Notes:</dt><dd class="notes">Lorem ipsum dolor sit amet, consectetur adipiscing elit, sed do eiusmod tempor incididunt ut labore et dolore magna aliqua. Ut enim ad minim veniam, quis nostrud exercitation ullamco laboris nisi ut aliquip ex ea commodo consequat.</dd></div>
  </dl>
</section>

</body>
</html>
```